We need a flyer design to promote Penhallow & Tibbs Landscaping and Lawn Maintenance.

The flyer needs to be have:-
1) A great head line ( When quality matters)
2) A really awesome offer ( no obligation free trial mow)
3) A sense of scarcity (Due to time restraints, we can only take limited number of free lawn jobs. This offer is only available to the first 20 callers)
4) A call to action (Call now to avoid disappointment)
5) Contact details (Penhallow & Tibbs Landscaping and Lawn Maintenance 0452 786 305)

The layout of the entire flyer should come across to potential customers as

1) simple to understand what Penhallow & Tibbs offer (not overcrowd with messages; the main aim is to communicate across our services.)

The list of services that Penhallow & Tibbs provide will be:-

- Lawn Mowing - Pruning - Weeding
- Mulching - Edging - Hedging
- Trimming - Fertilising - Garden maintenance
- Weekly, fortnightly or monthly programs

Thank you.

```html
<!DOCTYPE html>
<html lang="en">
<head>
<meta charset="utf-8">
<title>Penhallow &amp; Tibbs Landscaping – Flyer</title>
<link href="https://fonts.googleapis.com/css2?family=Great+Vibes&family=Arimo:wght@700&display=swap" rel="stylesheet">
<style>
  :root {
    --page-bg: #e9e4da;
    --paper: #ffffff;
    --brand-brown: #3d2a1e;
    --leaf-light: #a6d46a;
    --leaf-pale: #dcefc6;
    --forest: #3f7a22;
    --maroon: #5a1f17;
  }
  * { box-sizing: border-box; margin: 0; padding: 0; }
  html, body { width: 1200px; height: 913px; overflow: hidden; }
  body { background: var(--page-bg); position: relative; }

  .flyer {
    position: absolute; left: 302px; top: 90px;
    width: 587px; height: 754px;
    background: var(--paper);
    box-shadow: 0 2px 10px rgba(0,0,0,0.18);
    overflow: hidden;
  }
  .flyer__top-glow {
    position: absolute; left: 0; top: 0; width: 100%; height: 184px;
    background: linear-gradient(90deg, var(--leaf-pale) 0%, #ffffff 20%, #ffffff 100%);
  }
  .flyer__bottom-glow {
    position: absolute; left: 0; top: 523px; width: 100%; height: 231px;
    background: linear-gradient(90deg, #ffffff 0%, #ffffff 62%, var(--leaf-pale) 100%);
  }

  .business {
    position: absolute; left: 0; top: 20px; width: 100%; text-align: center;
    font-family: "Arimo", sans-serif; font-weight: 700; color: var(--brand-brown);
  }
  .business__name { font-size: 32px; line-height: 38px; }
  .business__services { font-size: 19px; line-height: 26px; margin-top: 8px; }

  .headline {
    position: absolute; left: 0; top: 112px; width: 100%; text-align: center;
    font-family: "Great Vibes", cursive; font-weight: 400; font-size: 58px;
    color: var(--forest); line-height: 70px;
  }

  .band { position: absolute; left: 0; width: 100%; height: 25px; }
  .band--upper { top: 184px; background: linear-gradient(90deg, var(--leaf-light) 0%, var(--leaf-pale) 55%, var(--leaf-light) 100%); }
  .band--lower { top: 499px; height: 24px; background: linear-gradient(90deg, #ffffff 0%, var(--leaf-pale) 40%, var(--leaf-light) 100%); }

  .photo { position: absolute; top: 209px; height: 290px; }
  .photo--home {
    left: 0; width: 391px;
    background: linear-gradient(180deg, #d8dcd2 0%, #c7b9a2 40%, #8a8070 60%, #5d8f3a 78%, #4f8430 100%);
  }
  .photo--play {
    left: 393px; width: 194px;
    background: linear-gradient(180deg, #5f8a3b 0%, #7da454 45%, #a9c67f 70%, #6ea03f 100%);
  }

  .offer {
    position: absolute; left: 0; top: 528px; width: 100%; text-align: center;
    font-family: "Great Vibes", cursive; font-size: 50px; color: var(--maroon); line-height: 60px;
  }
  .call {
    position: absolute; left: 0; top: 584px; width: 100%; text-align: center;
    font-family: "Arimo", sans-serif; font-weight: 700; font-size: 35px; line-height: 42px;
    color: var(--forest);
  }

  .services {
    position: absolute; left: 0; top: 632px; width: 100%;
    list-style: none; text-align: center;
  }
  .services__item {
    display: block; margin: 0 auto; width: 370px; height: 21px; line-height: 21px;
    font-family: "Arimo", sans-serif; font-weight: 700; font-size: 16px; color: var(--maroon);
    background: linear-gradient(90deg, transparent 0%, var(--leaf-pale) 8%, #ffffff 22%, #ffffff 78%, var(--leaf-pale) 92%, transparent 100%);
  }

  .terms {
    position: absolute; left: 188px; top: 722px; width: 210px; text-align: center;
    font-family: "Arimo", sans-serif; font-weight: 700; font-size: 7.5px; line-height: 9.5px;
    color: var(--maroon);
  }
</style>
</head>
<body>
  <main class="flyer">
    <div class="flyer__top-glow"></div>
    <div class="flyer__bottom-glow"></div>

    <header class="business">
      <h1 class="business__name">Penhallow &amp; Tibbs</h1>
      <p class="business__services">Landscaping and Lawn Maintenance</p>
    </header>

    <h2 class="headline">When Quality Matters</h2>

    <div class="band band--upper"></div>
    <div class="photo photo--home" role="img" aria-label="Photo of a modern house with a manicured front lawn, shaped shrubs and a curved concrete path"></div>
    <div class="photo photo--play" role="img" aria-label="Photo of a child swinging from a tree branch over a green lawn"></div>
    <div class="band band--lower"></div>

    <p class="offer">No Obligation Free trial mow</p>
    <p class="call">CALL:0452 786 305 NOW!</p>

    <ul class="services">
      <li class="services__item">Mulching-Edging-Hedging</li>
      <li class="services__item">Lawn Mowing-Pruning-Weeding</li>
      <li class="services__item">Trimming-Fertilising-Garden maintenence</li>
      <li class="services__item">Weekly, fortnightly or monthly programs</li>
    </ul>

    <p class="terms">Due to time restraints, we can only take limited number of free lawn jobs. This offer is only available for the first 20 callers</p>
  </main>
</body>
</html>
```